trading data display webpage

We have build a rough wireframe of the two webpages that we want to display .The two wireframes are attached as a pdf document.
there will be login page. after login , the user will see the index page. that is the first page of the wireframe.

what we are displaying is essentially spread data. we are taking the difference in prices are two places and displaying the data. some calculations are done and is shown in the grid.

below the grid we show the behaviour on a graph. we will use bubble chart. I did not find a sample, hence have thrown in a placeholder.

this is time series data ( changes daily) and hence we need to check the behaviour.

the second wire frame shows how the user will choose the source price points and the destination price points.
we are talking here of natural gas prices hence the reference to source prices and destination prices.

you need to design the page/ pages such that the end-user loves it and is easy to use. the intent here is easy to use and easy to understand.
this will be responsive webpage since the end user will check it out on a tablet or a smartphone.

so if possible tell us how the navigation bar, the button bar, etc should fall when the screen size decreases.

I have uploaded 2 files. one is the wireframe ( pdf document) and second is the logo file.

please also let us know where to place the logo.

Target Market(s)

the target market is traders and data analyst

Industry/Entity Type

Build

Colors

Designer to choose colors to be used in the design.

Requirements
Must have
• 1. design for the web.
2. but think how the design will look when the screen size decreases.
3. tell if possible what screen components to keep and what to hide.

```html
<!DOCTYPE html>
<html lang="en">
<head>
<meta charset="utf-8">
<title>Spreadline – Spread Data</title>
<link rel="stylesheet" href="https://fonts.googleapis.com/css2?family=Figtree:wght@400;500;600;700&display=swap">
<style>
:root{
  --bg:#e9edf1;
  --panel:#ffffff;
  --line:#dde3e8;
  --heading:#5e6b74;
  --text:#1f2225;
  --muted:#6d7478;
  --accent:#1a9ee6;
  --brand:#2e6fb5;
  --cyan:#8fdff0;
  --red:#f46a64;
  --green:#86c093;
  --pink:#fba6c6;
  --yellow:#fddd78;
}
*{box-sizing:border-box;margin:0;padding:0}
html,body{width:1200px;height:1200px;overflow:hidden}
body{background:var(--bg);font-family:"Figtree",Arial,sans-serif;color:var(--text);position:relative}
.abs{position:absolute}
.brand{left:231px;top:48px;display:flex;align-items:center;gap:12px}
.brand-dot{width:40px;height:40px;border-radius:50%;background:var(--brand)}
.brand-name{font-size:30px;font-weight:700;color:var(--brand)}
.help{left:879px;top:34px;font-size:11px;color:var(--text)}
.logout{left:966px;top:30px;width:60px;height:23px;border:1px solid #a9b1b6;border-radius:12px;background:#fff;font-size:12px;font-weight:600;display:flex;align-items:center;justify-content:center}
.tab{top:152px;height:34px;width:143px;background:#fff;border:1px solid var(--line);border-bottom:none;display:flex;font-size:12px;font-weight:600;color:var(--muted);z-index:2}
.tab .pin{width:34px;border-right:1px solid var(--line);display:flex;align-items:center;justify-content:center}
.tab .label{flex:1;display:flex;align-items:center;justify-content:center}
.tab.active{color:var(--text);height:35px}
.panel{left:199px;top:185px;width:866px;height:1100px;background:var(--panel);border:1px solid #d3d9de}
.section-title{left:231px;font-size:15px;font-weight:600;color:var(--heading);letter-spacing:.2px}
.rule{left:231px;width:781px;height:1px;background:var(--line)}
.select{top:251px;width:231px;height:35px;border:1px solid #d3dbe0;border-radius:2px;background:linear-gradient(#fbfcfd,#f1f4f6);display:flex}
.select span{flex:1;display:flex;align-items:center;padding-left:16px;font-size:14px;color:var(--muted)}
.select i{width:33px;border-left:1px solid #d3dbe0;display:flex;align-items:center;justify-content:center;background:#fff}
.seg{top:359px;height:32px;display:flex;border:1px solid #cfd8de;background:#f7f9fa;font-size:12px;color:var(--muted)}
.seg div{display:flex;align-items:center;justify-content:center;border-right:1px solid #dde3e8}
.seg div:last-child{border-right:none}
.seg div.on{background:#e8edf0}
.days{left:229px;width:200px;border-radius:16px;overflow:hidden}
.span{left:704px;width:177px;height:34px;border-radius:2px}
table{left:227px;top:473px;width:806px;border-collapse:collapse;border:1px solid var(--line);font-size:14px;table-layout:fixed}
thead tr{height:37px;background:#fff}
thead th{font-weight:600;text-align:left;border-top:1px solid #cfe0e8}
tbody td{height:40.5px;border-top:1px solid var(--line);border-left:1px solid var(--line);color:var(--muted)}
th{border-left:1px solid var(--line)}
th:first-child,td:first-child{border-left:none}
.card{top:919px;height:300px;border:1px solid #d3dde3;background:#fff}
.card h3{height:38px;border-bottom:1px solid #e1e7eb;background:linear-gradient(#fff,#f8fafb);font-size:13px;font-weight:600;display:flex;align-items:center;justify-content:center}
</style>
</head>
<body>
<div class="abs brand"><div class="brand-dot"></div><div class="brand-name">Spreadline</div></div>
<div class="abs help">Help &amp; Support</div>
<div class="abs logout">Logout</div>

<div class="abs tab active" style="left:227px"><div class="pin"><svg width="12" height="17" viewBox="0 0 12 17"><path d="M6 0a6 6 0 0 0-6 6c0 4 6 11 6 11s6-7 6-11a6 6 0 0 0-6-6z" fill="var(--accent)"/><circle cx="6" cy="6" r="2.2" fill="#fff"/></svg></div><div class="label">EAST</div></div>
<div class="abs tab" style="left:376px"><div class="pin"><svg width="12" height="17" viewBox="0 0 12 17"><path d="M6 0a6 6 0 0 0-6 6c0 4 6 11 6 11s6-7 6-11a6 6 0 0 0-6-6z" fill="#7a858c"/><circle cx="6" cy="6" r="2.2" fill="#fff"/></svg></div><div class="label">CENTRAL</div></div>
<div class="abs tab" style="left:525px"><div class="pin"><svg width="12" height="17" viewBox="0 0 12 17"><path d="M6 0a6 6 0 0 0-6 6c0 4 6 11 6 11s6-7 6-11a6 6 0 0 0-6-6z" fill="#7a858c"/><circle cx="6" cy="6" r="2.2" fill="#fff"/></svg></div><div class="label">WEST</div></div>

<div class="abs panel"></div>

<div class="abs section-title" style="top:210px">CHOOSE LOCATIONS</div>
<div class="abs rule" style="top:236px"></div>
<div class="abs select" style="left:229px"><span>Source Indices</span><i><svg width="10" height="14" viewBox="0 0 10 14"><path d="M5 0l5 6H0zM5 14L0 8h10z" fill="var(--accent)"/></svg></i></div>
<div class="abs select" style="left:701px"><span>Destination Indices</span><i><svg width="10" height="14" viewBox="0 0 10 14"><path d="M5 0l5 6H0zM5 14L0 8h10z" fill="var(--accent)"/></svg></i></div>

<div class="abs section-title" style="top:318px">CHOOSE PERIOD OF TIME</div>
<div class="abs rule" style="top:344px"></div>
<div class="abs seg days"><div class="on" style="width:70px">5 Days</div><div style="width:61px">7 Days</div><div style="width:69px">18 Days</div></div>
<div class="abs seg span"><div class="on" style="width:92px">Month</div><div style="width:85px">Year</div></div>

<div class="abs section-title" style="top:438px">RESULTS FOUND</div>
<table class="abs">
  <colgroup><col style="width:120px"><col style="width:108px"><col style="width:103px"><col style="width:100px"><col style="width:117px"><col style="width:114px"><col style="width:144px"></colgroup>
  <thead><tr><th style="padding-left:11px">Spread Name</th><th style="padding-left:25px">Avg sprd</th><th style="text-align:center">+ve prob</th><th style="text-align:center">-ve prob</th><th style="text-align:center">spike prob</th><th style="text-align:center">avg supply</th><th style="text-align:center">supply cut_prob</th></tr></thead>
  <tbody>
    <tr><td style="padding-left:16px">Spread1</td><td style="padding-left:25px">Item 1</td><td></td><td></td><td></td><td></td><td></td></tr>
    <tr><td style="padding-left:16px">Spread1</td><td style="padding-left:25px">Item 1</td><td></td><td></td><td></td><td></td><td></td></tr>
    <tr><td style="padding-left:16px">Spread1</td><td style="padding-left:25px">Item 1</td><td></td><td></td><td></td><td></td><td></td></tr>
    <tr><td style="padding-left:16px">Spread1</td><td style="padding-left:25px">Item 1</td><td></td><td></td><td></td><td></td><td></td></tr>
    <tr><td style="padding-left:16px">Spread1</td><td style="padding-left:25px">Item 1</td><td></td><td></td><td></td><td></td><td></td></tr>
    <tr><td style="padding-left:16px">Spread1</td><td style="padding-left:25px">Item 1</td><td></td><td></td><td></td><td></td><td></td></tr>
    <tr><td style="padding-left:16px">Spread1</td><td style="padding-left:25px">Item 1</td><td></td><td></td><td></td><td></td><td></td></tr>
    <tr><td style="padding-left:16px">Spread1</td><td style="padding-left:25px">Item 1</td><td></td><td></td><td></td><td></td><td></td></tr>
  </tbody>
</table>

<div class="abs section-title" style="top:885px">GRAPHIC RESULTS</div>

<div class="abs card" style="left:226px;width:335px">
  <h3>Spread v/s Supply</h3>
  <svg width="333" height="262" viewBox="0 0 333 262">
    <g transform="rotate(-90 166 138)" fill="none" stroke-width="34">
      <circle cx="166" cy="138" r="83" stroke="var(--red)" stroke-dasharray="42 480" stroke-dashoffset="-1.5"/>
      <circle cx="166" cy="138" r="83" stroke="var(--green)" stroke-dasharray="84 438" stroke-dashoffset="-46"/>
      <circle cx="166" cy="138" r="83" stroke="var(--pink)" stroke-dasharray="81 441" stroke-dashoffset="-133"/>
      <circle cx="166" cy="138" r="83" stroke="var(--yellow)" stroke-dasharray="149 373" stroke-dashoffset="-217"/>
      <circle cx="166" cy="138" r="83" stroke="var(--cyan)" stroke-dasharray="151 371" stroke-dashoffset="-369"/>
    </g>
  </svg>
</div>

<div class="abs card" style="left:597px;width:436px">
  <h3>Spreads Across Time</h3>
  <svg width="434" height="262" viewBox="0 0 434 262">
    <rect x="92" y="121" width="73" height="120" fill="var(--cyan)" stroke="#7fcde0"/>
    <rect x="177" y="72" width="73" height="169" fill="var(--red)" stroke="#e35a55"/>
    <rect x="261" y="39" width="73" height="202" fill="var(--green)" stroke="#74ad81"/>
  </svg>
</div>
</body>
</html>
```